FUN, COLORFUL, AND FAMILY CONCERT THAT CALLED BELLOMARA

A fun, colorful and modern poster. The theme this year is green and yellow, but please use other colors such as Neon or new combinations, patterns, cool design pattern or even splashes background. The name of the event is BELLOMARA. I want the Bellomara name to stand out and the date as well. Make the website name highlighted so other will go to the website and buy tickets to the concert. The date will be July, 11th, 2015. start time will be 4pm. Location at The Harlow Center @ Kessington University. Tickets will be $15 Adults $12 kids under 12 $5 under 5. I will send the old poster to give you a idea, but I want this year poster to be more of an eye catcher. I am still on the hiring process for the 4 bands will have so leave space for that as well. You can use circle or square or patterns for the photos. I like clear colors as well on the background or patterns. BE YOURSELF & CREATE THIS POSTER FROM YOUR HEART <3

Target Market(s)

everyone.

Industry/Entity Type

University

Font styles to use
Serif

Requirements
Must have
• the small bellomara logo on the bottom corner. Real people having fun in a concert ..please clear picture nothing blurry!
Nice to have
• brighter and white on the letters for Belomara. highlight Bellomara name, date, and the website (make those bigger). You can use circle, splashes, cool patterns for the date.
Should not have
• be boring ... it needs to be fun and an eye catcher

```html
<!DOCTYPE html>
<html lang="en">
<head>
<meta charset="utf-8">
<title>Bellomara 2015 Poster</title>
<link rel="stylesheet" href="https://fonts.googleapis.com/css2?family=Dancing+Script:wght@700&family=Arimo:wght@400;700&family=Questrial&family=Oswald:wght@400;600&display=swap">
<style>
  :root {
    --ink-dark: #141306;
    --glow-yellow: #ffe838;
    --glow-lime: #b6f23a;
    --glow-green: #3fbf2a;
    --band-yellow: #dcd84a;
    --band-yellow-light: #f4f19a;
    --band-edge: #c9c63a;
    --ribbon-green: #6aa22d;
    --ticket-brown: #7a3316;
    --title-brown: #4a1608;
    --frame-line: #f7f3dc;
    --number-gold: #ffd84a;
    --paper: #ffffff;
    --page-bg: #e9e6dc;
  }
  * { box-sizing: border-box; margin: 0; padding: 0; }
  html, body { width: 956px; height: 1200px; overflow: hidden; background: var(--page-bg); }
  .poster {
    position: relative; width: 956px; height: 1200px;
    background: var(--paper); padding: 12px;
  }
  .poster-inner {
    position: relative; width: 100%; height: 100%; overflow: hidden;
    background: var(--ink-dark);
  }
  .bokeh-art {
    position: absolute; inset: 0;
    background:
      radial-gradient(circle at 52% 66%, rgba(255,250,190,1) 0, rgba(255,232,56,.85) 9%, rgba(255,232,56,0) 30%),
      radial-gradient(circle at 18% 62%, rgba(255,232,56,.9) 0, rgba(255,232,56,0) 22%),
      radial-gradient(circle at 12% 44%, rgba(210,230,60,.55) 0, rgba(210,230,60,0) 14%),
      radial-gradient(circle at 82% 38%, rgba(255,225,60,.75) 0, rgba(255,225,60,0) 18%),
      radial-gradient(circle at 64% 24%, rgba(182,242,58,.7) 0, rgba(63,191,42,0) 22%),
      radial-gradient(circle at 40% 34%, rgba(63,191,42,.55) 0, rgba(63,191,42,0) 16%),
      radial-gradient(circle at 88% 66%, rgba(182,242,58,.55) 0, rgba(182,242,58,0) 18%),
      radial-gradient(circle at 30% 86%, rgba(255,210,40,.6) 0, rgba(255,210,40,0) 18%),
      radial-gradient(circle at 80% 88%, rgba(120,200,50,.45) 0, rgba(0,0,0,0) 16%),
      radial-gradient(circle at 8% 10%, rgba(0,0,0,.6) 0, rgba(0,0,0,0) 30%),
      linear-gradient(180deg, #1a1a06 0%, #3e3c0c 30%, #5a5a10 55%, #33480e 78%, #161405 100%);
  }
  .frame-lines { position: absolute; inset: 0; }
  .date-badge {
    position: absolute; left: 42px; top: 170px; width: 208px; height: 208px;
    border-radius: 50%;
    background: radial-gradient(circle at 50% 35%, #e6e3d4 0%, #b0ae9e 60%, #8a887c 100%);
    border: 4px solid #fff3a0;
    box-shadow: 0 0 28px rgba(255,232,56,.7);
    color: var(--paper); text-align: center; font-family: "Oswald", sans-serif;
  }
  .date-day { position: absolute; left: 0; right: 0; top: 26px; font-size: 96px; font-weight: 600; line-height: 1; text-shadow: 0 2px 4px rgba(0,0,0,.35); }
  .date-day sup { font-size: 30px; font-weight: 400; vertical-align: top; position: relative; top: 8px; }
  .date-month { position: absolute; left: 0; right: 0; top: 132px; font-size: 34px; letter-spacing: .5px; text-shadow: 0 2px 4px rgba(0,0,0,.35); }
  .event-title {
    position: absolute; left: 0; right: 0; top: 565px; text-align: center;
    font-family: "Dancing Script", cursive; font-weight: 700; font-size: 205px; line-height: 1;
    color: var(--paper);
    -webkit-text-stroke: 7px var(--title-brown); paint-order: stroke fill;
    text-shadow: 0 6px 12px rgba(0,0,0,.45), 0 0 40px rgba(255,240,120,.6);
  }
  .venue-band {
    position: absolute; left: 0; right: 0; top: 835px; height: 118px;
    background: linear-gradient(180deg, var(--band-yellow-light) 0%, var(--band-yellow) 100%);
    border-top: 14px solid var(--band-edge);
    text-align: center; font-family: "Arimo", sans-serif; font-size: 31px; color: #121212;
    padding-top: 12px; line-height: 1.35;
  }
  .tickets { position: absolute; left: 0; right: 0; top: 990px; text-align: center; }
  .tickets-label {
    position: relative; display: inline-block; background: var(--ribbon-green);
    color: var(--paper); font-family: "Arimo", sans-serif; font-size: 30px;
    padding: 4px 44px; z-index: 2;
  }
  .tickets-prices {
    margin: -6px auto 0; width: 680px; height: 78px;
    background: var(--ticket-brown); color: var(--paper);
    font-family: "Arimo", sans-serif; font-size: 31px; line-height: 84px;
    border-left: 26px solid var(--ribbon-green); border-right: 26px solid var(--ribbon-green);
  }
  .tickets-prices .sep { opacity: .6; margin: 0 12px; }
  .footer-rule { position: absolute; left: 20px; right: 20px; top: 1100px; height: 2px; background: var(--frame-line); opacity: .8; }
  .brand-mark {
    position: absolute; left: 24px; top: 1118px; display: flex; align-items: center; gap: 8px;
    font-family: "Arimo", sans-serif; font-weight: 700; font-size: 26px; color: var(--paper);
  }
  .brand-mark .square { width: 18px; height: 18px; background: var(--paper); }
  .website {
    position: absolute; left: 330px; top: 1120px;
    font-family: "Arimo", sans-serif; font-size: 30px; color: var(--paper);
  }
</style>
</head>
<body>
<main class="poster">
  <div class="poster-inner">
    <div class="bokeh-art" role="img" aria-label="Glowing neon green and yellow bokeh lights with a bright burst of light behind the title"></div>

    <svg class="frame-lines" width="932" height="1176" viewBox="0 0 932 1176" aria-hidden="true">
      <g fill="none" stroke="var(--frame-line)" stroke-width="2">
        <rect x="18" y="18" width="896" height="1080" opacity=".55"/>
        <path d="M540 40 H300 V255"/>
        <path d="M578 95 V262 H400"/>
        <path d="M645 40 H885 V255"/>
        <path d="M607 95 V262 H785"/>
        <path d="M300 315 V510 H540"/>
        <path d="M400 292 H578 V455"/>
        <path d="M885 315 V510 H645"/>
        <path d="M785 292 H607 V455"/>
      </g>
      <g fill="var(--number-gold)" font-family="Questrial, sans-serif" font-size="92" text-anchor="middle">
        <text x="430" y="190">1</text>
        <text x="760" y="190">2</text>
        <text x="430" y="430">3</text>
        <text x="760" y="430">4</text>
      </g>
    </svg>

    <div class="date-badge">
      <div class="date-day">11<sup>TH</sup></div>
      <div class="date-month">JULY 2015</div>
    </div>

    <h1 class="event-title">Bellomara</h1>

    <section class="venue-band">
      <p>The Harlow Center @ <strong>Kessington University</strong></p>
      <p>Show starts at <strong>4pm</strong> Doors open at 3pm</p>
    </section>

    <section class="tickets">
      <div class="tickets-label">Tickets will be</div>
      <div class="tickets-prices">$15 Adults<span class="sep">|</span>$12 kids under 12<span class="sep">|</span>$5 under 5</div>
    </section>

    <div class="footer-rule"></div>
    <div class="brand-mark"><span class="square"></span>BELLOMARA</div>
    <p class="website">Buy tickets @ www.bellomarapc.com</p>
  </div>
</main>
</body>
</html>
```